Web app UI design

This web app has been built and the UI needs a refresh.

Attached are the pages which need the refresh.

The web app is for a cyber security product/service and customers are inputting their details.

```html
<!DOCTYPE html>
<html lang="en">
<head>
<meta charset="utf-8">
<title>Trustline — App Screens</title>
<link rel="stylesheet" href="https://fonts.googleapis.com/css2?family=Inter:wght@300;400;500;600;700;800&display=swap">
<style>
:root{
  --board:#b3b3b3;
  --blue:#1a8cff;
  --btn:#1e90ff;
  --navy:#2d3246;
  --navy-top:#2f3447;
  --active:#2a4470;
  --page:#f4f5f9;
  --card:#ffffff;
  --ink:#2d3246;
  --ink-strong:#1b1d4a;
  --muted:#6b6f80;
  --line:#d6d8e0;
  --soft-blue:#e8f2ff;
}
*{box-sizing:border-box;margin:0;padding:0}
html,body{width:1200px;height:2635px;overflow:hidden}
body{position:relative;background:var(--board);font-family:"Inter",sans-serif;color:var(--ink)}
.backdrop{position:absolute;inset:0}
.screen{position:absolute;left:61px;width:1079px;overflow:hidden}

/* hero */
.hero{top:100px;height:573px}
.hero-photo{position:absolute;inset:0;background:linear-gradient(100deg,#3b3f4b 0%,#4a4e59 40%,#6d7079 52%,#55585f 60%,#3a3d48 100%)}
.search-card{position:absolute;left:382px;top:171px;width:336px;height:195px;background:#fff;border-radius:8px;padding:20px 24px}
.search-card h1{font-weight:300;font-size:24px;letter-spacing:5px;text-align:center;color:#555b66}
.field{position:relative;border:1px solid var(--line);border-radius:4px;height:42px;display:flex;align-items:center;padding:0 12px;font-size:11px;color:#3a3f52;background:#fff}
.field label{position:absolute;top:-6px;left:10px;background:#fff;padding:0 3px;font-size:8.5px;color:#7d8190}
.search-card .field{margin-top:30px}
.btn{display:inline-flex;align-items:center;justify-content:center;height:28px;padding:0 15px;border-radius:4px;font-size:11px;font-weight:600;letter-spacing:.4px;text-transform:uppercase}
.btn-primary{background:var(--btn);color:#fff;box-shadow:0 2px 6px rgba(30,144,255,.35)}
.btn-ghost{border:1px solid #9a9eab;color:#3a3f52;font-weight:500;background:#fff}
.search-card .btn{width:100%;height:32px;margin-top:16px}

/* app */
.app{background:var(--page)}
.sidebar{position:absolute;left:0;top:0;bottom:0;width:195px;background:var(--navy)}
.brand{position:absolute;left:24px;top:22px;font-size:16px;font-weight:400;letter-spacing:3px;color:#c8cbd6}
.collapse{position:absolute;left:181px;top:20px;width:24px;height:24px;border-radius:50%;background:#fff;display:flex;align-items:center;justify-content:center;z-index:2}
.collapse span{width:16px;height:16px;border-radius:50%;background:var(--btn);display:flex;align-items:center;justify-content:center}
.nav{position:absolute;left:12px;right:0;top:73px;list-style:none}
.nav li{position:relative;height:32px;margin-bottom:6px;display:flex;align-items:center;padding-left:12px;font-size:12.5px;color:#e6e8ef;gap:10px;width:171px;border-radius:4px}
.nav li svg{width:14px;height:14px}
.nav li.active{background:var(--active);color:var(--btn)}
.nav li.active::after{content:"";position:absolute;right:-12px;top:0;width:5px;height:32px;background:var(--btn);border-radius:3px 0 0 3px}
.nav .chev{position:absolute;right:12px}
.main{position:absolute;left:213px;top:0;width:849px;bottom:0}
.topbar{position:absolute;left:0;top:9px;width:849px;height:48px;background:var(--navy-top);border-radius:4px;display:flex;align-items:center;padding:0 16px;color:#fff;font-size:12.5px;gap:10px}
.topbar .tools{margin-left:auto;display:flex;align-items:center;gap:14px}
.avatar{position:relative;width:30px;height:30px;border-radius:50%;background:linear-gradient(135deg,#8fa8d8,#5a6fa8)}
.avatar::after{content:"";position:absolute;right:-1px;bottom:-1px;width:8px;height:8px;border-radius:50%;background:#2ecc71;border:1.5px solid var(--navy-top)}
.page-title{position:absolute;top:84px;font-size:21px;font-weight:700;color:var(--ink)}
.page-sub{position:absolute;top:118px;font-size:11.5px;color:var(--muted)}
.panel{position:absolute;left:0;width:849px;background:var(--card);border-radius:6px;box-shadow:0 2px 8px rgba(40,45,70,.06);padding:33px 18px 18px}
.grid{display:grid;grid-template-columns:1fr 1fr;column-gap:16px;row-gap:30px}
.actions{display:flex;gap:12px;margin-top:18px}
.footer{position:absolute;left:0;width:849px;text-align:center;font-size:11.5px;color:#7d8190}

/* plans */
.plans{position:absolute;left:0;top:153px;display:flex;gap:20px}
.plan{width:268px;height:420px;background:#fff;border-radius:10px;padding:19px 19px;box-shadow:0 2px 8px rgba(40,45,70,.06)}
.plan-head{display:flex;gap:14px;align-items:center}
.plan-icon{width:54px;height:54px;border-radius:8px;background:var(--soft-blue);display:flex;align-items:center;justify-content:center}
.plan-head small{display:block;font-size:13.5px;color:#5a5f73}
.plan-head strong{display:block;font-size:18px;font-weight:700;color:var(--ink-strong)}
.plan p{margin-top:20px;font-size:12px;line-height:22px;color:#6b6f80}
.price{margin-top:22px;font-size:40px;font-weight:800;color:var(--ink-strong);letter-spacing:-.5px}
.price span{font-size:15px;font-weight:400;color:#6b6f80;margin-left:6px;letter-spacing:0}
.plan h3{margin-top:10px;font-size:13.5px;font-weight:700;color:var(--ink-strong)}
.plan ul{list-style:none;margin-top:12px}
.plan li{display:flex;align-items:center;gap:10px;font-size:12px;color:#6b6f80;height:27px}
.plan .btn{width:100%;margin-top:15px;font-size:10.5px}

/* verify info */
.facts{display:flex;gap:0;align-items:center;margin-top:-15px}
.fact{display:flex;gap:12px;align-items:center}
.fact i{width:34px;height:34px;border-radius:50%;background:var(--btn);display:flex;align-items:center;justify-content:center}
.fact small{display:block;font-size:10px;color:#7d8190}
.fact b{display:block;font-size:12.5px;font-weight:500;color:#1f2233;margin-top:3px}
</style>
</head>
<body>

<svg class="backdrop" width="1200" height="2635" viewBox="0 0 1200 2635" aria-hidden="true">
  <path d="M0 0 H705 C735 160 735 420 650 560 C570 690 470 760 410 772 L0 772 V870 C-10 870 0 870 0 870 Z" fill="#1a8cff"/>
  <path d="M0 772 H410 C300 830 120 880 0 870 Z" fill="#1a8cff"/>
  <path d="M1200 1730 C1160 1725 1130 1730 1100 1740 L1140 1740 L1140 1970 L1200 1970 Z" fill="#1a8cff"/>
  <path d="M560 1970 C600 1920 640 1900 700 1885 L1140 1885 V1970 Z" fill="#1a8cff"/>
  <path d="M500 2039 C530 2000 545 1985 560 1970 H1140 V2039 Z" fill="#1a8cff"/>
  <path d="M410 2535 C420 2570 430 2610 440 2635 H1200 V2535 Z" fill="#1a8cff"/>
</svg>

<!-- Landing search -->
<section class="screen hero">
  <div class="hero-photo" role="img" aria-label="Dark photograph of two security cameras mounted on a striped wall"></div>
  <div class="search-card">
    <h1>TRUSTLINE</h1>
    <div class="field"><label>Companies name, ABN or ACN</label>Name/ABN/ACN</div>
    <div class="btn btn-primary">Search</div>
  </div>
</section>

<!-- Profile -->
<section class="screen app" style="top:772px;height:496px">
  <aside class="sidebar">
    <div class="brand">TRUSTLINE</div>
    <ul class="nav">
      <li class="active"><svg viewBox="0 0 14 14"><path d="M7 1 1 6.5h2V13h3V9h2v4h3V6.5h2z" fill="currentColor"/></svg>Home<svg class="chev" viewBox="0 0 10 10" width="10" height="10"><path d="M2 3.5 5 6.5 8 3.5" stroke="currentColor" fill="none" stroke-width="1.4"/></svg></li>
      <li><svg viewBox="0 0 14 14"><circle cx="7" cy="4" r="3" fill="currentColor"/><path d="M1 13c0-3.5 3-5 6-5s6 1.5 6 5z" fill="currentColor"/></svg>Profile</li>
      <li><svg viewBox="0 0 14 14"><path d="M2 5h10v8H2z" fill="currentColor"/><path d="M4.5 5V3.5a2.5 2.5 0 0 1 5 0V5" stroke="currentColor" fill="none" stroke-width="1.4"/></svg>Subscription</li>
      <li><svg viewBox="0 0 14 14"><rect x="1" y="1" width="12" height="12" rx="2" fill="currentColor"/><path d="M4 7l2 2 4-4" stroke="#2d3246" fill="none" stroke-width="1.6"/></svg>Verify</li>
    </ul>
  </aside>
  <div class="collapse"><span><svg width="8" height="8" viewBox="0 0 8 8"><path d="M5 1.5 2.5 4 5 6.5" stroke="#fff" fill="none" stroke-width="1.4"/></svg></span></div>
  <div class="main">
    <div class="topbar">
      <svg width="16" height="16" viewBox="0 0 16 16"><circle cx="7" cy="7" r="5" stroke="#fff" fill="none" stroke-width="1.6"/><path d="M11 11l3.5 3.5" stroke="#fff" stroke-width="1.6"/></svg>Search (Ctrl+/)
      <div class="tools">
        <svg width="18" height="18" viewBox="0 0 18 18" fill="none" stroke="#fff" stroke-width="1.3"><path d="M2 4h8M6 2v2M4 4c1 3 3 5 5 6M8 4c-1 3-3 5-5 6M10 16l3-7 3 7M11 14h4"/></svg>
        <svg width="15" height="15" viewBox="0 0 15 15" fill="none" stroke="#fff" stroke-width="1.3"><rect x="1" y="1" width="5" height="5"/><rect x="9" y="1" width="5" height="5"/><rect x="1" y="9" width="5" height="5"/><rect x="9" y="9" width="5" height="5"/></svg>
        <svg width="15" height="15" viewBox="0 0 15 15" fill="none" stroke="#fff" stroke-width="1.3"><path d="M12.5 9.5A6 6 0 0 1 5.5 2.5a6 6 0 1 0 7 7z"/></svg>
        <svg width="16" height="16" viewBox="0 0 16 16" fill="none" stroke="#fff" stroke-width="1.3"><path d="M3 12h10l-1.5-2V7a3.5 3.5 0 0 0-7 0v3zM6.5 14h3"/><circle cx="12" cy="3" r="2.5" fill="#ff4d4f" stroke="none"/></svg>
        <div class="avatar" role="img" aria-label="User avatar"></div>
      </div>
    </div>
    <h2 class="page-title">Profile</h2>
    <p class="page-sub">Only your company name, ACN and ABN from below will be shared on your profile.</p>
    <div class="panel" style="top:152px;height:284px">
      <div class="grid">
        <div class="field"><label>Email</label>Enter Email Address</div>
        <div class="field"><label>Company Legal Name</label>Enter Company Legal Name</div>
        <div class="field"><label>ACN</label>Enter ACN Number</div>
        <div class="field"><label>ABN</label>Enter ABN Number</div>
        <div class="field"><label>Phone Number</label>Enter Phone Number</div>
        <div class="field"><label>Website URL</label>Enter Website URL</div>
      </div>
      <div class="actions"><span class="btn btn-primary">Save Changes</span><span class="btn btn-ghost">Cancel</span></div>
    </div>
    <p class="footer" style="top:468px">© 2022, Trustline</p>
  </div>
</section>

<!-- Subscription -->
<section class="screen app" style="top:1336px;height:634px">
  <aside class="sidebar">
    <div class="brand">TRUSTLINE</div>
    <ul class="nav">
      <li><svg viewBox="0 0 14 14"><path d="M7 1 1 6.5h2V13h3V9h2v4h3V6.5h2z" fill="currentColor"/></svg>Home</li>
      <li><svg viewBox="0 0 14 14"><circle cx="7" cy="4" r="3" fill="currentColor"/><path d="M1 13c0-3.5 3-5 6-5s6 1.5 6 5z" fill="currentColor"/></svg>Profile</li>
      <li class="active" style="margin-top:8px"><svg viewBox="0 0 14 14"><path d="M2 5h10v8H2z" fill="currentColor"/><path d="M4.5 5V3.5a2.5 2.5 0 0 1 5 0V5" stroke="currentColor" fill="none" stroke-width="1.4"/></svg>Subscription</li>
      <li><svg viewBox="0 0 14 14"><rect x="1" y="1" width="12" height="12" rx="2" fill="currentColor"/><path d="M4 7l2 2 4-4" stroke="#2d3246" fill="none" stroke-width="1.6"/></svg>Verify</li>
    </ul>
  </aside>
  <div class="collapse"><span><svg width="8" height="8" viewBox="0 0 8 8"><path d="M5 1.5 2.5 4 5 6.5" stroke="#fff" fill="none" stroke-width="1.4"/></svg></span></div>
  <div class="main">
    <div class="topbar">
      <svg width="16" height="16" viewBox="0 0 16 16"><circle cx="7" cy="7" r="5" stroke="#fff" fill="none" stroke-width="1.6"/><path d="M11 11l3.5 3.5" stroke="#fff" stroke-width="1.6"/></svg>Search (Ctrl+/)
      <div class="tools">
        <svg width="18" height="18" viewBox="0 0 18 18" fill="none" stroke="#fff" stroke-width="1.3"><path d="M2 4h8M6 2v2M4 4c1 3 3 5 5 6M8 4c-1 3-3 5-5 6M10 16l3-7 3 7M11 14h4"/></svg>
        <svg width="15" height="15" viewBox="0 0 15 15" fill="none" stroke="#fff" stroke-width="1.3"><rect x="1" y="1" width="5" height="5"/><rect x="9" y="1" width="5" height="5"/><rect x="1" y="9" width="5" height="5"/><rect x="9" y="9" width="5" height="5"/></svg>
        <svg width="15" height="15" viewBox="0 0 15 15" fill="none" stroke="#fff" stroke-width="1.3"><path d="M12.5 9.5A6 6 0 0 1 5.5 2.5a6 6 0 1 0 7 7z"/></svg>
        <svg width="16" height="16" viewBox="0 0 16 16" fill="none" stroke="#fff" stroke-width="1.3"><path d="M3 12h10l-1.5-2V7a3.5 3.5 0 0 0-7 0v3zM6.5 14h3"/><circle cx="12" cy="3" r="2.5" fill="#ff4d4f" stroke="none"/></svg>
        <div class="avatar" role="img" aria-label="User avatar"></div>
      </div>
    </div>
    <h2 class="page-title">Subscription</h2>
    <p class="page-sub">This info below will be shown on your profile page</p>
    <div class="plans">
      <article class="plan">
        <div class="plan-head"><div class="plan-icon"><svg width="26" height="26" viewBox="0 0 26 26"><circle cx="13" cy="13" r="12" fill="#9cc8ff"/><path d="M13 1a12 12 0 0 0 0 24z" fill="var(--btn)"/></svg></div><div><small>For individuals</small><strong>Bronze</strong></div></div>
        <p>Lorem ipsum dolor sit amet doloroli sitiol conse ctetur adipiscing elit.</p>
        <div class="price">$85<span>/monthly</span></div>
        <h3>What’s included</h3>
        <ul>
          <li><svg width="14" height="14" viewBox="0 0 14 14"><circle cx="7" cy="7" r="7" fill="var(--btn)"/><path d="M4 7.2l2 2 4-4" stroke="#fff" fill="none" stroke-width="1.5"/></svg>All analytics features</li>
          <li><svg width="14" height="14" viewBox="0 0 14 14"><circle cx="7" cy="7" r="7" fill="var(--btn)"/><path d="M4 7.2l2 2 4-4" stroke="#fff" fill="none" stroke-width="1.5"/></svg>Up to 250,000 tracked visits</li>
          <li><svg width="14" height="14" viewBox="0 0 14 14"><circle cx="7" cy="7" r="7" fill="var(--btn)"/><path d="M4 7.2l2 2 4-4" stroke="#fff" fill="none" stroke-width="1.5"/></svg>Normal support</li>
          <li><svg width="14" height="14" viewBox="0 0 14 14"><circle cx="7" cy="7" r="7" fill="var(--btn)"/><path d="M4 7.2l2 2 4-4" stroke="#fff" fill="none" stroke-width="1.5"/></svg>Up to 3 team members</li>
        </ul>
        <div class="btn btn-primary">Subscribed</div>
      </article>
      <article class="plan">
        <div class="plan-head"><div class="plan-icon"><svg width="26" height="26" viewBox="0 0 26 26"><circle cx="13" cy="13" r="12" fill="#9cc8ff"/><path d="M13 1a12 12 0 0 0 0 24z" fill="var(--btn)"/></svg></div><div><small>For individuals</small><strong>Silver</strong></div></div>
        <p>Lorem ipsum dolor sit amet doloroli sitiol conse ctetur adipiscing elit.</p>
        <div class="price">$85<span>/monthly</span></div>
        <h3>What’s included</h3>
        <ul>
          <li><svg width="14" height="14" viewBox="0 0 14 14"><circle cx="7" cy="7" r="7" fill="var(--btn)"/><path d="M4 7.2l2 2 4-4" stroke="#fff" fill="none" stroke-width="1.5"/></svg>All analytics features</li>
          <li><svg width="14" height="14" viewBox="0 0 14 14"><circle cx="7" cy="7" r="7" fill="var(--btn)"/><path d="M4 7.2l2 2 4-4" stroke="#fff" fill="none" stroke-width="1.5"/></svg>Up to 250,000 tracked visits</li>
          <li><svg width="14" height="14" viewBox="0 0 14 14"><circle cx="7" cy="7" r="7" fill="var(--btn)"/><path d="M4 7.2l2 2 4-4" stroke="#fff" fill="none" stroke-width="1.5"/></svg>Normal support</li>
          <li><svg width="14" height="14" viewBox="0 0 14 14"><circle cx="7" cy="7" r="7" fill="var(--btn)"/><path d="M4 7.2l2 2 4-4" stroke="#fff" fill="none" stroke-width="1.5"/></svg>Up to 3 team members</li>
        </ul>
        <div class="btn btn-primary">Subscribed</div>
      </article>
      <article class="plan">
        <div class="plan-head"><div class="plan-icon"><svg width="26" height="26" viewBox="0 0 26 26"><circle cx="13" cy="13" r="12" fill="#9cc8ff"/><path d="M13 1a12 12 0 0 0 0 24z" fill="var(--btn)"/></svg></div><div><small>For individuals</small><strong>Gold</strong></div></div>
        <p>Lorem ipsum dolor sit amet doloroli sitiol conse ctetur adipiscing elit.</p>
        <div class="price">$85<span>/monthly</span></div>
        <h3>What’s included</h3>
        <ul>
          <li><svg width="14" height="14" viewBox="0 0 14 14"><circle cx="7" cy="7" r="7" fill="var(--btn)"/><path d="M4 7.2l2 2 4-4" stroke="#fff" fill="none" stroke-width="1.5"/></svg>All analytics features</li>
          <li><svg width="14" height="14" viewBox="0 0 14 14"><circle cx="7" cy="7" r="7" fill="var(--btn)"/><path d="M4 7.2l2 2 4-4" stroke="#fff" fill="none" stroke-width="1.5"/></svg>Up to 250,000 tracked visits</li>
          <li><svg width="14" height="14" viewBox="0 0 14 14"><circle cx="7" cy="7" r="7" fill="var(--btn)"/><path d="M4 7.2l2 2 4-4" stroke="#fff" fill="none" stroke-width="1.5"/></svg>Normal support</li>
          <li><svg width="14" height="14" viewBox="0 0 14 14"><circle cx="7" cy="7" r="7" fill="var(--btn)"/><path d="M4 7.2l2 2 4-4" stroke="#fff" fill="none" stroke-width="1.5"/></svg>Up to 3 team members</li>
        </ul>
        <div class="btn btn-primary">Subscribed</div>
      </article>
    </div>
    <p class="footer" style="top:605px">© 2022, Trustline</p>
  </div>
</section>

<!-- Verify Info -->
<section class="screen app" style="top:2039px;height:496px">
  <aside class="sidebar">
    <div class="brand">TRUSTLINE</div>
    <ul class="nav">
      <li><svg viewBox="0 0 14 14"><path d="M7 1 1 6.5h2V13h3V9h2v4h3V6.5h2z" fill="currentColor"/></svg>Home</li>
      <li><svg viewBox="0 0 14 14"><circle cx="7" cy="4" r="3" fill="currentColor"/><path d="M1 13c0-3.5 3-5 6-5s6 1.5 6 5z" fill="currentColor"/></svg>Profile</li>
      <li><svg viewBox="0 0 14 14"><path d="M2 5h10v8H2z" fill="currentColor"/><path d="M4.5 5V3.5a2.5 2.5 0 0 1 5 0V5" stroke="currentColor" fill="none" stroke-width="1.4"/></svg>Subscription</li>
      <li class="active" style="margin-top:8px"><svg viewBox="0 0 14 14"><rect x="1" y="1" width="12" height="12" rx="2" fill="currentColor"/><path d="M4 7l2 2 4-4" stroke="#2a4470" fill="none" stroke-width="1.6"/></svg>Verify</li>
    </ul>
  </aside>
  <div class="collapse"><span><svg width="8" height="8" viewBox="0 0 8 8"><path d="M5 1.5 2.5 4 5 6.5" stroke="#fff" fill="none" stroke-width="1.4"/></svg></span></div>
  <div class="main">
    <div class="topbar">
      <svg width="16" height="16" viewBox="0 0 16 16"><circle cx="7" cy="7" r="5" stroke="#fff" fill="none" stroke-width="1.6"/><path d="M11 11l3.5 3.5" stroke="#fff" stroke-width="1.6"/></svg>Search (Ctrl+/)
      <div class="tools">
        <svg width="18" height="18" viewBox="0 0 18 18" fill="none" stroke="#fff" stroke-width="1.3"><path d="M2 4h8M6 2v2M4 4c1 3 3 5 5 6M8 4c-1 3-3 5-5 6M10 16l3-7 3 7M11 14h4"/></svg>
        <svg width="15" height="15" viewBox="0 0 15 15" fill="none" stroke="#fff" stroke-width="1.3"><rect x="1" y="1" width="5" height="5"/><rect x="9" y="1" width="5" height="5"/><rect x="1" y="9" width="5" height="5"/><rect x="9" y="9" width="5" height="5"/></svg>
        <svg width="15" height="15" viewBox="0 0 15 15" fill="none" stroke="#fff" stroke-width="1.3"><path d="M12.5 9.5A6 6 0 0 1 5.5 2.5a6 6 0 1 0 7 7z"/></svg>
        <svg width="16" height="16" viewBox="0 0 16 16" fill="none" stroke="#fff" stroke-width="1.3"><path d="M3 12h10l-1.5-2V7a3.5 3.5 0 0 0-7 0v3zM6.5 14h3"/><circle cx="12" cy="3" r="2.5" fill="#ff4d4f" stroke="none"/></svg>
        <div class="avatar" role="img" aria-label="User avatar"></div>
      </div>
    </div>
    <h2 class="page-title">Verify Info</h2>
    <p class="page-sub">This info below will be shown on your profile page</p>
    <div class="panel" style="top:153px;height:284px">
      <div class="facts">
        <div class="fact" style="width:280px"><i><svg width="12" height="12" viewBox="0 0 12 12"><rect x="2" y="1" width="8" height="10" fill="#fff"/><path d="M4 3h1M7 3h1M4 5h1M7 5h1M4 7h1M7 7h1" stroke="var(--btn)"/></svg></i><div><small>Company Legal Name</small><b>Northwind Ledger Group</b></div></div>
        <div class="fact" style="width:158px"><i><svg width="12" height="12" viewBox="0 0 12 12"><path d="M2 1h5l3 3v7H2z" fill="#fff"/><path d="M4 6h4M4 8h4" stroke="var(--btn)"/></svg></i><div><small>ACN</small><b>111111</b></div></div>
        <div class="fact"><i><svg width="12" height="12" viewBox="0 0 12 12"><path d="M2 1h5l3 3v7H2z" fill="#fff"/><path d="M4 6h4M4 8h4" stroke="var(--btn)"/></svg></i><div><small>ABN</small><b>222222</b></div></div>
      </div>
      <div class="grid" style="margin-top:30px">
        <div class="field"><label>BSB</label>Enter BSB Number</div>
        <div class="field"><label>Account</label>Enter Account Number</div>
      </div>
      <div class="actions"><span class="btn btn-primary">Save Verify Data</span><span class="btn btn-ghost">Cancel</span></div>
    </div>
    <p class="footer" style="top:469px">© 2022, Trustline</p>
  </div>
</section>

</body>
</html>
```